Copperfield Growth Institute is changing lives and needs a state of the art PageLoom Business Web

We are looking for lots of WOW factor. We need a state of the art website that inspires people to take action toward changing their life. We have some award winning trademarked programs that we are looking to introduce through our website.

The Top Portion will have a place holder for a welcome video (currently being recorded) and this brief description of the business along side of it:
=====================================================
Let’s face it. Life is hard. Being human isn’t easy for any of us. Here, at the Copperfield Growth Institute, we understand that simple truth. We know that having a strong self-worth first requires you to be aware of your value as a Human Being. Human potential is the HIGHEST value that creation has to offer.

Regardless of whether you see it through the eyes of evolution or through the eyes of religion, the truth of the matter is that Human Beings are of significant value. Abundance is our birthright! Our focus is on developing that human potential.

There is only one thing holding you back from experiencing overflowing abundance – YOU! Ask yourself, why haven’t I experienced that true transformation, in my life, that attracts abundance?

What if there was a way to remove the uncertainty tied to the labyrinth of life? What if you no longer have to be a victim of the unpredictable? Well, the good news is – Its Possible! There is an amazing amount of potential locked away deep inside you. Potential that has the capacity to release you from your current patterns of thinking and launch a complete turning point in your life.

The Copperfield Growth Institute recognizes this potential, often before you recognize it in yourself, and is excited to partner with you on your journey to becoming an unstoppable force. We look forward to resourcing you with the tools and training that will help you synchronize your desire and your direction with your destiny!
============================================================

Under the welcome / intro block, we would like to have a gallery that scrolls through pictures, and inspirational quotes. We can also use this to advertise
our services and special deals on programs.

Next section can outline our lanes of business or focus areas:

High Performance Living
Business Coaching & Consultancy
Digital Resources Center

Here is the template we would like to leverage: https://pageloom-sites.example/theme/harvestline
or you can be creative and provide one you think would work best....

Should have some awesome photos, descriptions, etc....

Here are some samples to model after:

https://velmorabox.example/
https://www.kv7-mentoring.example/
http://derekosgoodby.example/

https://fenwickroutecrew.example/talk/?c=fnwk-se-bo&frtc=frt-core&gclid=QzXbTkLmNpRsVwYa-93tyhhb7RTKcPMqVTzZTwLo-QRAPiZAxHzT_K_QzXB

https://orlando-tebbit.example/
https://www.thecortexloft.example/
https://www.hollisvane.example/

Target Market(s)

Business Leaderships and anyone interested in personal development and growth

Industry/Entity Type

Leadership

Coding

Coded - Design and coding required

Font styles to use
Serif
Sans Serif
Decorative
Script

Colors

Designer to choose colors to be used in the design.

Requirements
Must have
• Business Name, Logo, and brief introduction paragraph. Must have space for the welcome video.
• We do not have any current site but do already own the domain for it:
• https://cgigrow.example/ is the PageLoom site we will be using once we choice a winner to work with
• Must use our Taglines:
• Shaping the existence of individuals, organizations, and communities...
• Turn your days into a rolling parade of wonder!
• =====================================================
• Would like music to softly play in back ground when people land on the page. This song could repeat in the background: https://www.vidstreamr.example/watch?v=QKTw7mZpLxa&list=ZRt4HbWqYcNmKdP8VsLe31JxfTuAoGh2N&index=4
• You can also cycle through the entire soundtrack of the MIDNIGHT CARAVAN - all those songs work perfectly with our themes
• You must also blend the content available on this site with the new site:
• https://www.harlowbrightcircle.example/dorianwexley
Nice to have
• would like music to softly play in back ground when people land on the page. This song could repeat in the softly in the background: https://www.vidstreamr.example/watch?v=QKTw7mZpLxa&list=ZRt4HbWqYcNmKdP8VsLe31JxfTuAoGh2N&index=4
Should not have
• Ads, empty white space, negative perspectives, etc....

```html
<!DOCTYPE html>
<html lang="en">
<head>
<meta charset="utf-8">
<title>Copperfield Growth Institute</title>
<link rel="stylesheet" href="https://fonts.googleapis.com/css2?family=Montserrat:wght@300;400;500&family=Noto+Serif:ital,wght@0,400;1,400&family=Courgette&display=swap">
<style>
:root{
  --navy:#2b3276;
  --navy-deep:#272d6e;
  --royal:#3a4aa8;
  --charcoal:#3f3f3f;
  --nav:#3b3b3b;
  --ink:#333;
  --muted:#666;
  --paper:#fff;
  --mist:#f3f3f4;
  --line:#dcdcdc;
}
*{box-sizing:border-box;margin:0;padding:0}
html,body{width:1200px;height:3550px;overflow:hidden;background:var(--paper)}
body{font-family:"Montserrat",sans-serif;color:var(--ink);position:relative}
.abs{position:absolute}
.serif{font-family:"Noto Serif",serif}

/* header */
.brand{left:123px;top:38px;width:200px;text-align:center;color:var(--navy);font-family:"Noto Serif",serif;font-size:22px;line-height:1.15}
.brand-mark{display:block;width:34px;height:34px;border-radius:50%;background:var(--navy);margin:0 auto 8px}
.call{left:595px;top:62px;display:flex;align-items:center;gap:12px}
.call small{display:block;font-family:"Noto Serif",serif;font-size:12px;color:var(--muted)}
.call strong{display:block;font-size:23px;font-weight:500;color:var(--navy);letter-spacing:.5px}
.book{left:888px;top:57px;width:189px;height:49px;border:1px solid var(--navy);color:var(--navy);font-family:"Noto Serif",serif;font-size:12px;display:flex;align-items:center;justify-content:center}
.nav{left:123px;top:161px;width:954px;height:43px;background:var(--nav);display:flex}
.nav a{flex:1;display:flex;align-items:center;justify-content:center;color:#fff;font-size:12px;letter-spacing:1.4px;text-decoration:none;border-right:1px solid #555}
.nav a.active{background:var(--royal)}

/* photo placeholders */
.photo{position:absolute}
.hero-photo{left:0;top:204px;width:1200px;height:447px;background:linear-gradient(100deg,#d9d6d1 0%,#b7c3cf 45%,#8fa1b3 70%,#4b5663 100%)}
.hero-caption{left:0;top:450px;width:599px;height:201px;background:var(--navy);color:#fff;padding:62px 0 0 123px;font-family:"Noto Serif",serif;font-size:27px;line-height:1.35}
.strip-photo{left:0;top:651px;width:599px;height:83px;background:linear-gradient(90deg,#e3e3e3,#c9c9c9)}
.slide-arrows{left:472px;top:681px;display:flex;gap:6px}
.slide-arrows span{width:20px;height:20px;border-radius:50%;background:rgba(0,0,0,.45);display:flex;align-items:center;justify-content:center}
.video-photo{left:599px;top:651px;width:601px;height:653px;background:linear-gradient(135deg,#cfd3d6 0%,#9a9fa3 45%,#6e6f70 100%)}
.play{left:870px;top:947px}

/* welcome */
.welcome{left:0;top:734px;width:599px;height:655px;background:var(--paper);padding:76px 0 0 123px}
.welcome h1{font-weight:300;font-size:50px;color:#444;line-height:1}
.welcome h2{font-family:"Noto Serif",serif;font-weight:400;font-size:18px;color:var(--navy);margin-top:10px}
.welcome hr{width:100px;border:0;border-top:1px solid var(--navy);margin:18px 0 26px}
.welcome p{width:415px;font-size:11.4px;line-height:1.78;color:var(--muted);margin-bottom:16px}
.btn{display:inline-flex;align-items:center;justify-content:center;width:122px;height:41px;border:1px solid var(--navy);color:var(--navy);font-family:"Noto Serif",serif;font-size:12px}
.welcome .btn{margin-top:22px}

/* quote */
.quote{left:0;top:1389px;width:1200px;height:365px;background:linear-gradient(180deg,#f6f6f7,#eeeef0);text-align:center}
.quote p{position:absolute;left:240px;top:96px;width:720px;font-family:"Noto Serif",serif;font-style:italic;font-size:19.5px;line-height:1.55;color:var(--navy)}
.dots{position:absolute;left:0;top:284px;width:1200px;display:flex;justify-content:center;gap:8px}
.dots span{width:11px;height:11px;border-radius:50%;border:1px solid #777}

/* services */
.panel{position:absolute;width:600px;padding:0 0 0 123px}
.panel h3{font-family:"Noto Serif",serif;font-weight:400;font-size:29px;line-height:1.25;margin-bottom:16px}
.panel p{width:390px;font-size:11.6px;line-height:1.75;margin-bottom:28px}
.panel.dark{color:#fff}
.panel.dark .btn{border-color:#fff;color:#fff}
.panel.light h3{color:var(--navy)}
.panel.light p{color:var(--muted)}
.panel.right{padding-left:82px}
.notch{position:absolute;width:0;height:0;border-top:14px solid transparent;border-bottom:14px solid transparent}

/* footer */
.footer{left:0;top:2978px;width:1200px;height:572px;background:var(--navy-deep);color:#fff;text-align:center}
.footer .script{position:absolute;left:0;top:76px;width:1200px;font-family:"Courgette",cursive;font-size:19px}
.footer .phone{position:absolute;left:0;top:132px;width:1200px;font-size:40px;font-weight:300;letter-spacing:1px}
.footer .email{position:absolute;left:0;top:187px;width:1200px;font-size:14px}
.footer .pin{position:absolute;left:585px;top:248px}
.footer address{position:absolute;left:0;top:306px;width:1200px;font-style:normal;font-size:12px;line-height:1.7}
.footer .foot-brand{position:absolute;left:0;top:420px;width:1200px;font-family:"Noto Serif",serif;font-size:16px}
.footer .copy{position:absolute;left:0;top:482px;width:1200px;font-size:11px}
.social{position:absolute;left:1104px;top:82px;display:flex;flex-direction:column;gap:13px}
.social span{width:13px;height:13px;border-radius:50%;background:#fff}
</style>
</head>
<body>

<header>
  <div class="abs brand"><span class="brand-mark"></span>Copperfield Growth Institute</div>
  <div class="abs call">
    <svg width="20" height="34" viewBox="0 0 20 34" aria-hidden="true"><rect x="1" y="1" width="18" height="32" rx="3" fill="none" stroke="#888" stroke-width="1.6"/><line x1="7" y1="28" x2="13" y2="28" stroke="#888" stroke-width="1.6"/></svg>
    <div><small>Call Us Toll Free:</small><strong>555-018-2740</strong></div>
  </div>
  <a class="abs book">Book An Appointment</a>
  <nav class="abs nav">
    <a class="active">HOME</a><a>ABOUT US</a><a>SERVICES</a><a>NEWS</a><a>CONTACT</a>
  </nav>
</header>

<section>
  <div class="photo hero-photo" role="img" aria-label="Photo of two smiling business people meeting in front of a glass office tower"></div>
  <div class="abs hero-caption">Turn your days into a rolling<br>parade of wonder!</div>
  <div class="photo strip-photo" role="img" aria-label="Slider photo of a business handshake"></div>
  <div class="abs slide-arrows">
    <span><svg width="8" height="8" viewBox="0 0 8 8"><path d="M5 1 2 4l3 3" stroke="#fff" fill="none"/></svg></span>
    <span><svg width="8" height="8" viewBox="0 0 8 8"><path d="M3 1l3 3-3 3" stroke="#fff" fill="none"/></svg></span>
  </div>
  <div class="photo video-photo" role="img" aria-label="Welcome video placeholder showing a smiling man in a meeting room"></div>
  <svg class="abs play" width="60" height="60" viewBox="0 0 60 60" aria-label="Play welcome video"><circle cx="30" cy="30" r="27" fill="none" stroke="#fff" stroke-width="3"/><path d="M24 18 42 30 24 42Z" fill="#fff"/></svg>

  <div class="abs welcome">
    <h1>Welcome to</h1>
    <h2>Copperfield Growth Institute</h2>
    <hr>
    <p>Let’s face it. Life is hard. Being human isn’t easy for any of us. Here, at the Copperfield Growth Institute, we understand that simple truth. We know that having a strong self-worth first requires you to be aware of your value as a Human Being. Human potential is the HIGHEST value that creation has to offer.</p>
    <p>Regardless of whether you see it through the eyes of evolution or through the eyes of religion, the truth of the matter is that Human Beings are of significant value. Abundance is our birthright! Our focus is on developing that human potential.</p>
    <p>There is only one thing holding you back from experiencing overflowing abundance – YOU! Ask yourself, why haven’t I experienced that true transformation, in my life, that attracts abundance?</p>
    <a class="btn">About Us</a>
  </div>
</section>

<section class="abs quote">
  <p>“ Lorem ipsum dolor sit amet, consectetur adipiscing elit, sed do eiusmod tempor incididunt ut labore et dolore magna aliqua. Ut enim ad minim veniam, quis nostrud exercitation ullamco ”</p>
  <div class="dots"><span></span><span></span><span></span><span></span><span></span></div>
</section>

<section>
  <div class="panel dark" style="left:0;top:1754px;height:407px;background:var(--navy);padding-top:76px">
    <h3>High Performance<br>Living</h3>
    <p>Lorem ipsum dolor sit amet, consectetur adipiscing elit, sed do eiusmod tempor incididunt ut labore et dolore magna aliqua. Ut enim ad minim veniam, quis nostrud exercitation ullamco laboris nisi ut aliquip ex ea commodo consequat.</p>
    <a class="btn">Learn More</a>
  </div>
  <div class="photo" style="left:600px;top:1754px;width:600px;height:206px;background:linear-gradient(90deg,#c9ccd2,#8c929c 60%,#5b6068)" role="img" aria-label="Photo of a business team around a meeting table"></div>
  <div class="notch" style="left:600px;top:1840px;border-left:14px solid var(--navy)"></div>
  <div class="panel light right" style="left:600px;top:1960px;height:407px;background:var(--paper);padding-top:68px">
    <h3>Business Coaching and<br>Consultancy</h3>
    <p>Lorem ipsum dolor sit amet, consectetur adipiscing elit, sed do eiusmod tempor incididunt ut labore et dolore magna aliqua. Ut enim ad minim veniam, quis nostrud exercitation ullamco laboris nisi ut aliquip ex ea commodo consequat.</p>
    <a class="btn">Learn More</a>
  </div>
  <div class="photo" style="left:0;top:2161px;width:600px;height:206px;background:linear-gradient(90deg,#b9b3ab,#d9d3cc 50%,#8f8780)" role="img" aria-label="Photo of colleagues in a workshop discussion"></div>

  <div class="panel dark" style="left:0;top:2367px;height:407px;background:var(--charcoal);padding-top:76px">
    <h3>Digital Resources<br>Center</h3>
    <p>Lorem ipsum dolor sit amet, consectetur adipiscing elit, sed do eiusmod tempor incididunt ut labore et dolore magna aliqua. Ut enim ad minim veniam, quis nostrud exercitation ullamco laboris nisi ut aliquip ex ea commodo consequat.</p>
    <a class="btn">Learn More</a>
  </div>
  <div class="photo" style="left:600px;top:2367px;width:600px;height:206px;background:linear-gradient(90deg,#dfe3e6,#9ba6b1 60%,#4c5563)" role="img" aria-label="Photo of hands working on a tablet at a desk"></div>
  <div class="notch" style="left:600px;top:2450px;border-left:14px solid var(--charcoal)"></div>
  <div class="panel light right" style="left:600px;top:2573px;height:405px;background:var(--mist);padding-top:66px">
    <h3 style="color:#333">Need help or have a<br>question?</h3>
    <p style="font-size:13.5px;width:410px">Book your free 30 minute business consultation today. we are always here to help you.</p>
    <a class="btn">Consult Now!</a>
  </div>
  <div class="photo" style="left:0;top:2774px;width:600px;height:204px;background:linear-gradient(90deg,#6b5b52,#aab4c0 50%,#3b4250)" role="img" aria-label="Photo of smiling business professionals in suits"></div>
</section>

<footer class="abs footer">
  <div class="script">We’d love to hear from you.</div>
  <div class="phone">P. 555-018-2740</div>
  <div class="email">e. info@cgigrow.example</div>
  <svg class="pin" width="30" height="38" viewBox="0 0 30 38" aria-hidden="true"><path d="M15 2C8 2 3 7 3 14c0 9 12 21 12 21s12-12 12-21C27 7 22 2 15 2Z" fill="none" stroke="#fff" stroke-width="2"/><circle cx="15" cy="14" r="4" fill="none" stroke="#fff" stroke-width="2"/></svg>
  <address>1420 Alder Brook Ln. #204<br>Marden Falls, NC 27598</address>
  <div class="foot-brand">Copperfield Growth Institute</div>
  <div class="copy">© 2019 Copperfield Growth Institute.</div>
  <div class="social" aria-label="Social links"><span></span><span></span><span></span><span></span><span></span></div>
</footer>

</body>
</html>
```